Stationery Design Project

Hi All,

We need you to design stationary for a new Business and Accounting Advisory Firm. We have already got the logo designed and it is attached. If you could also if possible, match the fonts in your design to that on the logo’s provided.

What we need:
- Business Card
- A4 Letter head
- A4 Folders
- PPT template (Title page and regular page)

And what ever else you want to throw in.

We are in the process of getting the web site designed, however below is a list of websites which we like which will give you an understanding of the style that we are going for.

- plavoni.com
- brightfunnelo.com
- hourquillet.com
- artmarrowly.com

I look forward to your seeing your design.

Hi All,

I have just realised that I forgot that i need to include a Licensed Tallymasters image on the letter head, please find attaced as File 1. Could you please have this image in the bottom left header.

Regards,

Gareth

Industry/Entity Type

Business

Requirements
Must have
• Outputs:
- Documents ready to print
- Generic editable information
- Pdf copies of the documents
- Word version of letterhead

```html
<!DOCTYPE html>
<html lang="en">
<head>
<meta charset="utf-8">
<title>Norwell Partners — Stationery</title>
<link rel="stylesheet" href="https://fonts.googleapis.com/css2?family=Crimson+Text:wght@400&family=Montserrat:wght@400&family=Open+Sans:wght@400;600&display=swap">
<style>
  :root {
    --navy: #2c4b8e;
    --blue: #3a5c9f;
    --teal: #46b4ca;
    --orange: #e57d24;
    --gold: #e8b23b;
    --paper: #ffffff;
    --ground: #efefef;
    --ink: #4a4a4a;
    --rule: #d7d7d7;
    --band: linear-gradient(90deg, var(--blue), var(--teal));
    --accent: linear-gradient(90deg, var(--orange), var(--gold));
  }
  * { box-sizing: border-box; margin: 0; padding: 0; }
  html, body { width: 1200px; height: 960px; overflow: hidden; }
  body { background: var(--ground); position: relative; font-family: "Open Sans", Arial, sans-serif; color: var(--ink); }
  .sheet { position: absolute; background: var(--paper); }

  .brand-name { font-family: "Crimson Text", Georgia, serif; color: var(--navy); font-weight: 400; white-space: nowrap; line-height: 1; }
  .brand-tag { font-family: "Montserrat", Arial, sans-serif; color: var(--navy); text-transform: none; white-space: nowrap; line-height: 1; }

  /* Letterhead */
  .letterhead { left: 215px; top: 107px; width: 338px; height: 519px; }
  .letterhead .lockup { position: absolute; top: 62px; left: 0; width: 100%; text-align: center; }
  .letterhead .brand-name { font-size: 15px; }
  .letterhead .brand-tag { font-size: 6px; letter-spacing: 2.6px; margin-top: 2px; }
  .letter-body { position: absolute; left: 53px; top: 131px; width: 262px; font-size: 6.6px; line-height: 8.7px; color: #555; }
  .letter-body p { margin-bottom: 8.7px; }
  .signature { position: absolute; left: 56px; top: 440px; width: 34px; height: 14px; background: #e7e9f3; border-radius: 3px; }
  .sheet-footer { position: absolute; left: 20px; right: 4px; top: 494px; display: flex; gap: 5px; font-size: 4.6px; color: #555; white-space: nowrap; }
  .sheet-footer span { display: flex; align-items: center; gap: 2px; }
  .dot { display: inline-block; width: 6px; height: 6px; border-radius: 50%; background: var(--blue); }
  .letterhead .base-band { position: absolute; left: 0; right: 0; bottom: 2px; height: 10px; background: var(--band); }
  .letterhead .base-line { position: absolute; left: 0; right: 0; bottom: 12px; height: 1px; background: var(--gold); }

  /* Folder */
  .folder { left: 645px; top: 82px; width: 432px; height: 546px; }
  .folder .spine { position: absolute; left: 0; top: 0; bottom: 0; width: 14px; border-right: 1px solid var(--rule); background: linear-gradient(90deg, #f4f4f4, #fff); }
  .folder .lockup { position: absolute; top: 170px; left: 14px; right: 0; text-align: center; }
  .folder .brand-name { font-size: 30px; }
  .folder .brand-tag { font-size: 11px; letter-spacing: 5.6px; margin-top: 8px; }
  .folder .url-band { position: absolute; left: 0; right: 0; top: 323px; height: 25px; background: var(--accent); color: #fff; font-size: 10px; letter-spacing: 1.4px; display: flex; align-items: center; justify-content: center; padding-left: 40px; }
  .folder .cover-band { position: absolute; left: 0; right: 0; top: 351px; bottom: 0; background: var(--band); }

  /* Business cards */
  .card { width: 165px; height: 94px; }
  .card-front { left: 83px; top: 672px; background: var(--band); text-align: center; }
  .card-front .brand-name { color: #fff; font-size: 11px; position: absolute; top: 48px; left: 0; width: 100%; }
  .card-back { left: 83px; top: 791px; height: 95px; }
  .card-back .lockup { position: absolute; left: 8px; top: 46px; width: 76px; text-align: center; }
  .card-back .brand-name { font-size: 9.5px; }
  .card-back .brand-tag { font-size: 3.5px; letter-spacing: 1.4px; margin-top: 2px; }
  .card-back .divider { position: absolute; left: 86px; top: 20px; width: 1px; height: 58px; background: var(--rule); }
  .card-back .details { position: absolute; left: 91px; top: 18px; font-size: 4.2px; line-height: 6.4px; color: #555; }
  .card-back .details .person { font-weight: 600; color: var(--navy); font-size: 5px; }
  .card-back .details .role { margin-bottom: 6px; }
  .card-back .details .row { display: flex; gap: 3px; align-items: flex-start; }
  .card-back .details .dot { width: 5px; height: 5px; margin-top: 1px; flex: none; }
  .card-back .base-line { position: absolute; left: 0; right: 0; bottom: 8px; height: 1px; background: var(--orange); }
  .card-back .base-band { position: absolute; left: 0; right: 0; bottom: 0; height: 6px; background: var(--blue); }

  /* Envelopes */
  .envelope-front { left: 291px; top: 686px; width: 410px; height: 195px; }
  .envelope-front .lockup { position: absolute; left: 46px; top: 20px; }
  .envelope-front .brand-name { font-size: 12px; }
  .envelope-front .brand-tag { font-size: 5px; letter-spacing: 2.2px; margin-top: 2px; }
  .envelope-front .return { position: absolute; left: 20px; top: 65px; font-size: 5.4px; display: flex; gap: 3px; align-items: center; color: #555; }
  .envelope-front .window { position: absolute; left: 19px; top: 76px; width: 127px; height: 40px; border: 1px solid #cfcfcf; border-radius: 5px; background: #ececec; }
  .envelope-front .base-line { position: absolute; left: 0; right: 0; bottom: 12px; height: 1.5px; background: var(--accent); }
  .envelope-front .base-band { position: absolute; left: 0; right: 0; bottom: 0; height: 10px; background: var(--band); }

  .envelope-back { left: 741px; top: 685px; width: 411px; height: 195px; }
  .envelope-back svg { position: absolute; left: 0; top: 0; }
  .envelope-back .brand-name { position: absolute; top: 22px; left: 0; width: 100%; text-align: center; color: #fff; font-size: 17px; }
</style>
</head>
<body>

<section class="sheet letterhead" aria-label="Letterhead">
  <div class="lockup">
    <div class="brand-name">Norwell Partners</div>
    <div class="brand-tag">Business Advisors</div>
  </div>
  <div class="letter-body">
    <p>Your Street Address<br>Your City, State&nbsp; Zip<br>Date</p>
    <p>First and Last Name of the Person to whom you are writing<br>Their Street Address<br>City, ST Zip</p>
    <p>Dear Mr./Ms. Full Name:</p>
    <p style="margin-bottom:0">You do not want to indent when you are using this format.&nbsp; This is the best format to use when you are writing a persuasive letter.&nbsp; You want to introduce yourself and the topic you are writing about to the reader.&nbsp; Remember that the first rule of writing is to know your audience.&nbsp; In a persuasive letter, you state your opinion or your feelings about something that is important to you after you have introduced yourself.&nbsp; You must sound as professional and passionate as possible.&nbsp; You do not want to belittle the reader or they will not finish reading your letter.&nbsp; Your letter needs to have the facts, reasons, and examples to support your position. Address issues that your reader may have in their argument.</p>
    <p>In a second paragraph, you must have solutions.&nbsp; Without solutions, you are only complaining. Offer assistance in solving the problem.&nbsp; Remind the reader where they can contact you.</p>
    <p style="margin-top:26px">Sincerely yours,</p>
  </div>
  <div class="signature" role="img" aria-label="Handwritten signature"></div>
  <div class="sheet-footer">
    <span><i class="dot"></i>Kerkstraat 42-B7, 5678 CD, Zwolle</span>
    <span><i class="dot"></i>555-018-2240</span>
    <span><i class="dot"></i>555-018-2249</span>
    <span><i class="dot"></i>info@norwellpartners.com</span>
    <span><i class="dot"></i>www.norwellpartners.com</span>
  </div>
  <div class="base-line"></div>
  <div class="base-band"></div>
</section>

<section class="sheet folder" aria-label="Presentation folder">
  <div class="spine"></div>
  <div class="lockup">
    <div class="brand-name">Norwell Partners</div>
    <div class="brand-tag">Business Advisors</div>
  </div>
  <div class="url-band">www.norwellpartners.com</div>
  <div class="cover-band"></div>
</section>

<section class="sheet card card-front" aria-label="Business card front">
  <div class="brand-name">Norwell Partners</div>
</section>

<section class="sheet card card-back" aria-label="Business card back">
  <div class="lockup">
    <div class="brand-name">Norwell Partners</div>
    <div class="brand-tag">Business Advisors</div>
  </div>
  <div class="divider"></div>
  <div class="details">
    <div class="person">Daniel Hartwig</div>
    <div class="role">Director</div>
    <div class="row"><i class="dot"></i><span>Kerkstraat 42-B7<br>5678 CD, Zwolle</span></div>
    <div class="row"><i class="dot"></i><span>555-018-2240</span></div>
    <div class="row"><i class="dot"></i><span>555-018-2249</span></div>
    <div class="row"><i class="dot"></i><span>daniel@norwellpartners.com</span></div>
    <div class="row"><i class="dot"></i><span>www.norwellpartners.com</span></div>
  </div>
  <div class="base-line"></div>
  <div class="base-band"></div>
</section>

<section class="sheet envelope-front" aria-label="Envelope front">
  <div class="lockup">
    <div class="brand-name">Norwell Partners</div>
    <div class="brand-tag">Business Advisors</div>
  </div>
  <div class="return"><i class="dot"></i>Kerkstraat 42-B7, 5678 CD, Zwolle</div>
  <div class="window"></div>
  <div class="base-line"></div>
  <div class="base-band"></div>
</section>

<section class="sheet envelope-back" aria-label="Envelope back">
  <svg width="411" height="70" viewBox="0 0 411 70" aria-hidden="true">
    <defs>
      <linearGradient id="flap-fill" x1="0" x2="1" y1="0" y2="0">
        <stop offset="0" stop-color="#3a5c9f"/>
        <stop offset="1" stop-color="#46b4ca"/>
      </linearGradient>
    </defs>
    <path d="M0 0 H411 L402 58 Q401 67 392 67 H20 Q11 67 10 58 Z" fill="url(#flap-fill)"/>
  </svg>
  <div class="brand-name">Norwell Partners</div>
</section>

</body>
</html>
```